Business Card Design Project

We need a business card design for a consultancy called 'Amber Ridge'. The design should communicate innovation and professionalism. The colors used should complement our logo. Please include source files for winning design.
Updates

Industry/Entity Type

Business

Colors

Designer to choose colors to be used in the design.

Requirements
Must have
• Card size should be 85mm x 50mm. The back side of the card should be the logo on a black background. The front side should display the name 'Amber Ridge' along with standard information. The front's design should graphically complement the back.
Nice to have
• Any graphical elements in the front the complement the back side (with the logo on a black background) would be a plus.

```html
<!DOCTYPE html>
<html lang="en">
<head>
<meta charset="utf-8">
<title>Amber Ridge – Business Card</title>
<link href="https://fonts.googleapis.com/css2?family=Macondo&display=swap" rel="stylesheet">
<style>
  :root {
    --backdrop: #5c2130;
    --card-black: #0b0b0b;
    --card-grain: #161616;
    --amber: #d0802c;
    --amber-deep: #b8661f;
    --amber-light: #e9a24a;
  }
  * { margin: 0; padding: 0; box-sizing: border-box; }
  html, body {
    width: 1200px; height: 833px; overflow: hidden;
    background: var(--backdrop);
    font-family: "Macondo", fantasy;
  }
  .stage { position: relative; width: 1200px; height: 833px; }
  .card {
    position: absolute; top: 214px;
    width: 449px; height: 259px; overflow: hidden;
    background: radial-gradient(ellipse at 50% 40%, var(--card-grain), var(--card-black) 75%);
  }
  .card--back { left: 131px; }
  .card--front { left: 620px; }
  .stripe {
    position: absolute; top: 0; bottom: 0; width: 5px;
    background: var(--amber-deep);
  }
  .card--back .stripe--one { left: 11px; }
  .card--back .stripe--two { left: 22px; }
  .card--front .stripe--one { left: 6px; }
  .card--front .stripe--two { left: 17px; }

  .brand-mark { position: absolute; }
  .card--back .brand-mark { left: 140px; top: 22px; }
  .brand-name {
    position: absolute; left: 0; right: 0; text-align: center;
    color: var(--amber); white-space: nowrap;
  }
  .card--back .brand-name { top: 188px; font-size: 42px; }

  .front-title {
    position: absolute; left: 28px; top: 4px;
    font-size: 48px; letter-spacing: 1px; color: var(--amber); white-space: nowrap;
  }
  .title-rule {
    position: absolute; left: 28px; right: 0; top: 64px; height: 3px;
    background: var(--amber-deep);
  }
  .contact {
    position: absolute; left: 42px; color: var(--amber);
    font-size: 27px; white-space: nowrap; letter-spacing: .5px;
  }
  .contact--tel { top: 80px; left: 44px; }
  .contact--email { top: 113px; left: 42px; font-size: 25px; }
  .contact--web { top: 229px; left: 35px; font-size: 19px; }

  .mini-brand { position: absolute; left: 352px; top: 165px; width: 90px; height: 90px; }
  .mini-brand .brand-mark { left: 23px; top: 0; }
  .mini-brand .brand-name { top: 66px; font-size: 15px; }
</style>
</head>
<body>
<main class="stage">
  <section class="card card--back" aria-label="Card back">
    <span class="stripe stripe--one"></span>
    <span class="stripe stripe--two"></span>
    <svg class="brand-mark" width="176" height="176" viewBox="0 0 176 176" aria-hidden="true">
      <circle cx="88" cy="88" r="86" fill="var(--amber)"/>
    </svg>
    <p class="brand-name">Amber Ridge</p>
  </section>

  <section class="card card--front" aria-label="Card front">
    <span class="stripe stripe--one"></span>
    <span class="stripe stripe--two"></span>
    <h1 class="front-title">AMBER RIDGE</h1>
    <span class="title-rule"></span>
    <p class="contact contact--tel">tel: 5550142873</p>
    <p class="contact contact--email">email: amber_ridge@mailnest.net</p>
    <p class="contact contact--web">website: www.amberridge.net</p>
    <div class="mini-brand">
      <svg class="brand-mark" width="44" height="44" viewBox="0 0 44 44" aria-hidden="true">
        <circle cx="22" cy="22" r="21" fill="var(--amber)"/>
      </svg>
      <p class="brand-name">Amber Ridge</p>
    </div>
  </section>
</main>
</body>
</html>
```